Marlowe Holdings LLC - Business Cards

Need the following information on the cards:

Name: Dean R Vossler
Title: Chief Executive Manager

Business address:
412 N Ridgeview Lane #118
Fernwood Falls, Il 60412

Phone: (555) 555-0148 - Business
KPV FFL license number: 5-21-xxx-xx-xx-04519
Email: dean.vossler@marloweholdingsffl.com

Target Market(s)

Firearm owners

Industry/Entity Type

Firearms industry,

Contact Information for Business Card

Contact number, name and title, web page address, email, business address and kpv license number,

Requirements
Must have
• Name, title, business address, phone numbers, KPV license numbers, web page address and email address.
Nice to have
• Cellphone number,

```html
<!DOCTYPE html>
<html lang="en">
<head>
<meta charset="UTF-8">
<title>Marlowe Holdings LLC – Business Cards</title>
<link href="https://fonts.googleapis.com/css2?family=Archivo:wght@700&family=Oswald:wght@500&family=Montserrat:wght@500;600&display=swap" rel="stylesheet">
<style>
  :root {
    --page: #ffffff;
    --card: #000000;
    --red: #d2202a;
    --white: #ffffff;
  }
  * { margin: 0; padding: 0; box-sizing: border-box; }
  html, body { width: 1200px; height: 1200px; overflow: hidden; background: var(--page); }
  .canvas { position: relative; width: 1200px; height: 1200px; }
  .card {
    position: absolute; left: 154px; width: 892px; height: 510px;
    background: var(--card); overflow: hidden;
  }
  .card--front { top: 61px; }
  .card--back { top: 628px; }

  .holder-name {
    position: absolute; left: 76px; top: 76px;
    font-family: "Archivo", Arial, sans-serif; font-weight: 700;
    font-size: 35px; letter-spacing: 1px; color: var(--white);
  }
  .holder-title {
    position: absolute; left: 76px; top: 112px;
    font-family: "Oswald", "Arial Narrow", sans-serif; font-weight: 500;
    font-size: 22px; color: var(--red);
  }
  .contact {
    position: absolute; left: 76px;
    font-family: "Montserrat", Arial, sans-serif; font-weight: 500;
    font-size: 17px; line-height: 21px; color: var(--white);
    display: flex; gap: 14px; align-items: flex-start;
  }
  .contact svg { width: 16px; height: 16px; fill: var(--red); flex: none; margin-top: 2px; }
  .contact--phone { top: 187px; }
  .contact--address { top: 229px; }
  .contact--email { top: 292px; }
  .license {
    position: absolute; left: 76px; top: 418px;
    font-family: "Montserrat", Arial, sans-serif; font-weight: 500;
    font-size: 17px; color: var(--white);
  }
  .license__number { color: var(--red); }

  .mascot-art {
    position: absolute; left: 473px; top: 63px; width: 419px; height: 382px;
    background: radial-gradient(ellipse at 55% 50%, #3a0a0d 0%, #1a0405 55%, var(--card) 80%);
  }

  .brand-name {
    position: absolute; left: 0; right: 0; top: 205px;
    text-align: center;
    font-family: "Montserrat", Arial, sans-serif; font-weight: 600;
    font-size: 40px; letter-spacing: 2px; color: var(--red);
  }
  .website {
    position: absolute; left: 0; right: 0; top: 430px;
    text-align: center;
    font-family: "Montserrat", Arial, sans-serif; font-weight: 500;
    font-size: 24px; color: var(--red);
  }
</style>
</head>
<body>
<div class="canvas">
  <section class="card card--front">
    <h1 class="holder-name">DEAN R. VOSSLER</h1>
    <p class="holder-title">Chief Executive Manager</p>

    <p class="contact contact--phone">
      <svg viewBox="0 0 24 24" aria-hidden="true"><path d="M6.6 10.8c1.4 2.8 3.8 5.1 6.6 6.6l2.2-2.2c.3-.3.7-.4 1-.2 1.1.4 2.3.6 3.6.6.6 0 1 .4 1 1V20c0 .6-.4 1-1 1C10.6 21 3 13.4 3 4c0-.6.4-1 1-1h3.5c.6 0 1 .4 1 1 0 1.3.2 2.5.6 3.6.1.3 0 .7-.2 1L6.6 10.8z"/></svg>
      <span>(555) 555-0148</span>
    </p>
    <p class="contact contact--address">
      <svg viewBox="0 0 24 24" aria-hidden="true"><path d="M12 2C8.1 2 5 5.1 5 9c0 5.2 7 13 7 13s7-7.8 7-13c0-3.9-3.1-7-7-7zm0 9.5a2.5 2.5 0 1 1 0-5 2.5 2.5 0 0 1 0 5z"/></svg>
      <span>412 N Ridgeview Lane<br>#118 Fernwood Falls, Il 60412</span>
    </p>
    <p class="contact contact--email">
      <svg viewBox="0 0 24 24" aria-hidden="true"><path d="M2 5h20v14H2V5zm2 2v.4l8 5 8-5V7H4z"/></svg>
      <span>dean.vossler@marloweholdingsffl.com</span>
    </p>

    <p class="license">KPV FFL license number: <span class="license__number">5-21-xxx-xx-xx-04519</span></p>

    <div class="mascot-art" role="img" aria-label="Red line illustration of a standing shepherd dog in profile"></div>
  </section>

  <section class="card card--back">
    <p class="brand-name">MARLOWE HOLDINGS LLC</p>
    <p class="website">yourwebsite.com</p>
  </section>
</div>
</body>
</html>
```